FALCON RIDGE SKY LEISURE SOCIETY

WE MAKE FLYING FUN AGAIN! We are a Semi Government Sport Aviation club that focuses on the highest quality of aviation training but in the spirit of Sport flying. The club is for aviation enthusiasts to come and share their passion with other club members to build their sport pilot skills.
Club Background and Structure: Club is Semi-Government and falls under the Coral Dunes Leisure Authority. We have seven Board Members that Shape the vision of the club. We have a CEO that take care of FRSLS as a whole and an Operations Manager that takes charge of Daily Flight Operations.
SPORT FLYING is different from a normal Pilots license due to the fact that the pilots fly as a hobby and fun and NOT for Commercial purposes . We would like a design to represent a professional but yet fun side of flying to showcase the "club" side (pilot family)
The club focuses on 3 types of Aircraft Fixed wing aircraft, Gyrocopters and Paramotor (NOTE: Paramotor will have their own web page, but the paramotor must be featured as one of the options. when the pilot chooses the paramotor it must link to paramotor web page)
The page must have the following MINIMUM requirements:
1. General page with logo and some nice pictures that feature both aircraft types (photos in files section)
2. "Get Started" tab that features the following sequence a: Choose your aircraft ( picture of Fixed wing and picture of gyrocopter and picture of paramotor)
b: Get a Introductory Flight.
2. "About us"
3. Services & Price
4. Our Team
5. Fleet
6. Bookings (pilots and introductory scenic flights)
7. Events (with calendar please)
8. Contact us
9. FAQ
10 Ground School
11 Other Sports and Activities
12 Our Partners

Requirements
Must have
• Professional design and easy to maintain and user friendlyness
Nice to have
• We have a booking system that needs to be connected to web page if possible
Should not have
• no clip art

```html
<!DOCTYPE html>
<html lang="en">
<head>
<meta charset="utf-8">
<title>Falcon Ridge Sky Leisure Society</title>
<link rel="stylesheet" href="https://fonts.googleapis.com/css2?family=Oswald:wght@400;500;600&family=Roboto:wght@400;500&family=Poppins:wght@400;500;600&display=swap">
<style>
:root{
  --purple:#4b3f9d;
  --purple-dark:#3d3387;
  --magenta:#b12f80;
  --magenta-deep:#9d2475;
  --heading:#a3287a;
  --teal:#3a86ab;
  --ink:#222;
  --body:#555;
  --muted:#8a8a8a;
  --field:#ececec;
  --white:#fff;
}
*{box-sizing:border-box;margin:0;padding:0}
html,body{width:1200px;height:5172px;overflow:hidden}
body{position:relative;background:var(--white);font-family:'Roboto',sans-serif;color:var(--body)}
.abs{position:absolute}
.btn{position:absolute;display:flex;align-items:center;justify-content:center;background:var(--teal);color:var(--white);font-family:'Roboto',sans-serif;font-weight:500;font-size:14px;text-transform:uppercase;box-shadow:0 4px 10px rgba(0,0,0,.25)}

/* header */
.site-header{position:absolute;left:0;top:0;width:1200px;height:118px;background:var(--white)}
.brand{position:absolute;left:112px;top:38px;display:flex;align-items:center;gap:10px}
.brand-mark{width:30px;height:30px;border-radius:50%;background:var(--purple)}
.brand-name{font-family:'Oswald',sans-serif;font-weight:500;font-size:28px;color:var(--purple);letter-spacing:1px}
.main-nav{position:absolute;left:345px;top:0;height:90px;display:flex;font-family:'Roboto',sans-serif;font-weight:500;font-size:12px;color:#222}
.main-nav span{display:flex;align-items:center;padding:0 12px;height:90px}
.main-nav .active{background:var(--purple);color:var(--white);padding:0 18px}
.book-now{left:930px;top:40px;width:158px;height:42px;font-size:13px}

/* hero */
.hero{position:absolute;left:0;top:118px;width:1200px;height:650px;background:linear-gradient(160deg,#5c6e3e 0%,#4f6a3a 35%,#6b7560 65%,#59604c 100%)}
.hero-title{position:absolute;left:600px;top:185px;width:520px;font-family:'Oswald',sans-serif;font-weight:500;font-size:58px;line-height:76px;color:var(--white);text-transform:uppercase}
.hero-text{position:absolute;left:600px;top:340px;width:490px;font-size:13px;line-height:26px;color:var(--white)}
.hero .btn{left:600px;top:404px;width:188px;height:50px;font-size:14px}
.hero-arrow{position:absolute;top:300px;width:46px;height:46px;border-radius:50%;background:rgba(0,0,0,.45);display:flex;align-items:center;justify-content:center}
.hero-dots{position:absolute;top:594px;left:564px;display:flex;gap:4px}
.hero-dots i{width:12px;height:12px;border-radius:50%;border:2px solid var(--white);display:block}
.hero-dots i.on{background:var(--white)}

/* about */
.about{position:absolute;left:0;top:768px;width:1200px;height:736px}
.eyebrow{position:absolute;left:112px;top:146px;font-family:'Oswald',sans-serif;font-size:16px;color:var(--heading);text-transform:uppercase}
.about h2{position:absolute;left:112px;top:178px;font-family:'Oswald',sans-serif;font-weight:400;font-size:30px;color:#222}
.about-copy{position:absolute;left:112px;top:262px;width:430px;font-size:13px;line-height:25px;color:#444}
.about-copy p{margin-bottom:12px}
.about .btn{left:112px;top:542px;width:188px;height:52px}
.about-photo{position:absolute;left:646px;top:125px;width:434px;height:487px;background:linear-gradient(180deg,#b9c6d6 0%,#9aa7b7 45%,#c0353e 75%,#8e8a86 100%);box-shadow:0 6px 16px rgba(0,0,0,.3)}
.side-label{position:absolute;left:1105px;top:520px;transform:rotate(-90deg);transform-origin:left top;font-family:'Oswald',sans-serif;font-weight:600;font-size:80px;color:rgba(160,40,122,.08);letter-spacing:4px}

/* services */
.services{position:absolute;left:0;top:1504px;width:1200px;height:794px;background:var(--purple)}
.section-title{position:absolute;left:0;width:1200px;text-align:center;font-family:'Oswald',sans-serif;font-weight:500;font-size:42px;text-transform:uppercase}
.title-rule{position:absolute;left:553px;width:94px;height:3px}
.services .section-title{top:62px;color:var(--white)}
.services .title-rule{top:128px;background:var(--white)}
.service-card{position:absolute;width:446px;height:256px;background:var(--white);border-radius:18px;overflow:hidden;box-shadow:0 6px 18px rgba(0,0,0,.25)}
.service-card.active{outline:4px solid #2f8fa9;outline-offset:-4px}
.service-media{position:absolute;left:0;top:0;width:172px;height:256px}
.service-card h3{position:absolute;left:188px;top:34px;font-family:'Oswald',sans-serif;font-weight:400;font-size:16px;color:#222;text-transform:uppercase}
.service-card p{position:absolute;left:188px;top:70px;width:240px;font-size:11px;line-height:22px;color:#666}
.service-arrow{position:absolute;left:188px;top:218px}

/* fleet */
.fleet{position:absolute;left:0;top:2298px;width:1200px;height:542px}
.fleet-frame{position:absolute;left:24px;top:40px;width:566px;height:492px;border:2px solid #b4337e}
.fleet-photo{position:absolute;left:0;top:2px;width:570px;height:480px;background:linear-gradient(180deg,#7f95a9 0%,#6f8a95 30%,#9fb0b5 55%,#3f6a7a 100%);box-shadow:0 6px 16px rgba(0,0,0,.3)}
.fleet h2{position:absolute;left:642px;top:72px;font-family:'Oswald',sans-serif;font-weight:500;font-size:42px;color:var(--heading)}
.fleet .rule{position:absolute;left:642px;top:130px;width:80px;height:3px;background:var(--purple)}
.fleet p{position:absolute;left:642px;top:158px;width:450px;font-size:13px;line-height:27.5px;color:#444}
.outline-btn{position:absolute;left:642px;top:340px;width:190px;height:54px;border:2px solid var(--teal);color:var(--teal);display:flex;align-items:center;justify-content:center;font-size:14px;font-weight:500;text-transform:uppercase}

/* team */
.team{position:absolute;left:0;top:2840px;width:1200px;height:712px}
.team .section-title{top:94px;color:var(--heading)}
.team .title-rule{top:152px;background:var(--purple);width:80px;left:560px}
.member{position:absolute;top:188px;width:316px;height:408px;border:1px solid #ddd;background:var(--white)}
.member-photo{position:absolute;left:9px;top:8px;width:298px;height:274px}
.member h4{position:absolute;left:0;top:298px;width:100%;text-align:center;font-family:'Poppins',sans-serif;font-weight:600;font-size:14px;color:#222}
.member .role{position:absolute;left:0;top:320px;width:100%;text-align:center;font-family:'Poppins',sans-serif;font-size:13px;color:#777}
.member-social{position:absolute;left:118px;top:352px;display:flex;gap:10px}
.member-social i{display:block;width:34px;height:34px;border:1px solid var(--magenta);position:relative}
.member-social i::after{content:"";position:absolute;left:11px;top:11px;width:10px;height:10px;border-radius:50%;background:var(--magenta)}
.team-dots{position:absolute;left:570px;top:638px;display:flex;gap:4px}
.team-dots i{width:12px;height:12px;border-radius:50%;border:2px solid var(--purple);display:block}
.team-dots i.on{background:var(--purple)}

/* bookings */
.bookings{position:absolute;left:0;top:3552px;width:1200px;height:516px;background:linear-gradient(180deg,#b3307f 0%,#a52a7c 60%,#9d2878 100%)}
.bookings .section-title{top:66px;color:var(--white)}
.bookings .title-rule{top:130px;background:var(--white);width:80px;left:560px}
.bookings-copy{position:absolute;left:140px;top:168px;width:920px;text-align:center;font-size:13px;line-height:27.5px;color:var(--white)}
.bookings-copy p{margin-bottom:16px}
.bookings .btn{left:506px;top:370px;width:188px;height:50px}

/* contact */
.contact{position:absolute;left:0;top:4068px;width:1200px;height:724px}
.contact-frame{position:absolute;left:112px;top:4px;width:458px;height:530px;border:2px solid var(--purple);border-radius:60px 0 60px 0}
.contact-photo{position:absolute;left:112px;top:62px;width:430px;height:480px;border-radius:60px 0 0 0;background:linear-gradient(160deg,#d0a24a 0%,#a07640 35%,#c23636 70%,#5c4a3e 100%);box-shadow:0 6px 16px rgba(0,0,0,.3)}
.contact h2{position:absolute;left:600px;top:126px;font-family:'Oswald',sans-serif;font-weight:500;font-size:42px;color:var(--heading)}
.field{position:absolute;background:var(--field);border-radius:4px;font-family:'Poppins',sans-serif;font-size:12px;color:#555;padding:0 10px;display:flex;align-items:center}
.field.area{align-items:flex-start;padding-top:14px}
.apply{position:absolute;left:600px;top:4610px;width:250px;height:52px;border-radius:26px;background:var(--teal);color:var(--white);font-family:'Poppins',sans-serif;font-weight:600;font-size:16px;display:flex;align-items:center;justify-content:center;gap:8px;box-shadow:0 4px 10px rgba(0,0,0,.25)}

/* footer */
.site-footer{position:absolute;left:0;top:4792px;width:1200px;height:380px;background:linear-gradient(180deg,var(--purple) 0%,#7a3a90 55%,#a02c7e 100%)}
.newsletter-title{position:absolute;left:0;top:14px;width:1200px;text-align:center;font-family:'Oswald',sans-serif;font-size:20px;color:var(--white);text-transform:uppercase}
.newsletter{position:absolute;left:292px;top:66px;width:614px;height:50px;border:2px solid var(--white);display:flex}
.newsletter .email{flex:1;background:var(--white);font-size:13px;color:#333;display:flex;align-items:center;padding-left:16px}
.newsletter .sub{width:204px;background:var(--teal);color:var(--white);font-family:'Oswald',sans-serif;font-size:20px;display:flex;align-items:center;justify-content:center}
.social{position:absolute;left:474px;top:142px;display:flex;gap:18px}
.social i{display:block;width:36px;height:36px;border:2px solid var(--white);border-radius:50%;position:relative}
.social i::after{content:"";position:absolute;left:11px;top:11px;width:10px;height:10px;border-radius:50%;background:var(--white)}
.footer-rule{position:absolute;left:112px;top:218px;width:976px;height:1px;background:rgba(255,255,255,.5)}
.footer-nav{position:absolute;left:0;top:250px;width:1200px;display:flex;justify-content:center;gap:28px;font-family:'Oswald',sans-serif;font-size:14px;color:var(--white);text-transform:uppercase}
.copyright{position:absolute;left:0;top:298px;width:1200px;text-align:center;font-size:14px;color:var(--white)}
</style>
</head>
<body>

<header class="site-header">
  <div class="brand"><span class="brand-mark"></span><span class="brand-name">FRSLS</span></div>
  <nav class="main-nav">
    <span class="active">HOME</span><span>ABOUT US</span><span>SERVICES &amp; PRICE</span><span>OUR TEAM</span><span>FLEET</span><span>EVENTS</span><span>FAQ</span><span>CONTACT</span>
  </nav>
  <div class="btn book-now">Book Now</div>
</header>

<section class="hero" role="img" aria-label="Aerial photo of a yellow gyrocopter flying over a green racetrack">
  <div class="hero-arrow" style="left:46px"><svg width="12" height="12" viewBox="0 0 12 12"><path d="M8 1 3 6l5 5" fill="none" stroke="#fff" stroke-width="2"/></svg></div>
  <div class="hero-arrow" style="left:1106px"><svg width="12" height="12" viewBox="0 0 12 12"><path d="M4 1l5 5-5 5" fill="none" stroke="#fff" stroke-width="2"/></svg></div>
  <h1 class="hero-title">Falcon Ridge Sky Leisure Society</h1>
  <p class="hero-text">FRSLS represents an excitingly unique place, where aviation sports enthusiasts come together to safely enjoy the adventures life has to offer.</p>
  <div class="btn">Get Started</div>
  <div class="hero-dots"><i></i><i></i><i class="on"></i><i></i><i></i></div>
</section>

<section class="about">
  <div class="side-label">ABOUT US</div>
  <div class="eyebrow">Welcome to</div>
  <h2>The Falcon Ridge Sky Leisure Society!</h2>
  <div class="about-copy">
    <p>FRSLS represents an excitingly unique place, where aviation sports enthusiasts come together to safely enjoy the adventures life has to offer.</p>
    <p>If you have long been searching for a place full of extraordinarily exciting sports and activities, FRSLS is where you belong</p>
    <p>We help the youth (and everyone reaching for the sky) discover engaging activities that provide a healthy challenge, promoting the growth of character. At the same time, we fully support the Coral Dunes vision and strategy of helping the youth engage</p>
  </div>
  <div class="btn">Read More</div>
  <div class="about-photo" role="img" aria-label="Three club members posing beside a red gyrocopter on the runway"></div>
</section>

<section class="services">
  <h2 class="section-title">Services</h2>
  <div class="title-rule"></div>

  <article class="service-card active" style="left:140px;top:180px">
    <div class="service-media" role="img" aria-label="Skydiver illustration on magenta" style="background:#b12f80"></div>
    <h3>Skydive</h3>
    <p>Experience the thrill of freefall skydiving and canopy flight with an experienced instructor! You deserve the best so come join our world class instructors and experience the thrill of a lifetime!</p>
    <svg class="service-arrow" width="40" height="14" viewBox="0 0 40 14"><path d="M0 7h37M31 1l6 6-6 6" fill="none" stroke="#b12f80" stroke-width="2.5"/></svg>
  </article>

  <article class="service-card" style="left:612px;top:180px">
    <div class="service-media" role="img" aria-label="Yellow gyrocopter with pilot and passenger" style="background:linear-gradient(180deg,#c9c2b4,#c8a040 60%,#8c7f6a)"></div>
    <h3>Flight Club</h3>
    <p>FRSLS offers crazy flights and joyful rides for passengers, as well as flight training courses and pilot permits for an impressive range of aircraft.Our club's imposing fleet includes fixed-wing light sports aircraft (LSA),</p>
    <svg class="service-arrow" width="40" height="14" viewBox="0 0 40 14"><path d="M0 7h37M31 1l6 6-6 6" fill="none" stroke="#b12f80" stroke-width="2.5"/></svg>
  </article>

  <article class="service-card" style="left:140px;top:462px">
    <div class="service-media" role="img" aria-label="Paramotor pilot flying over the sea" style="background:linear-gradient(180deg,#6f9fca,#3d6a96 60%,#2e4f73)"></div>
    <h3>Paramotor</h3>
    <p>The FRSLS Paramotor training program is split into three stages. The first stage covers ground handling. Over the course of 3 to 5 days, you'll learn the basics of the sport, including how the equipment</p>
    <svg class="service-arrow" width="40" height="14" viewBox="0 0 40 14"><path d="M0 7h37M31 1l6 6-6 6" fill="none" stroke="#b12f80" stroke-width="2.5"/></svg>
  </article>

  <article class="service-card" style="left:612px;top:462px">
    <div class="service-media" role="img" aria-label="Colourful parasail above the sea" style="background:linear-gradient(180deg,#d6a04a,#8fb4d4 45%,#3f7fa8)"></div>
    <h3>Parasail</h3>
    <p>Too much of anything is never a good thing. Or is it?Having too much fun never hurt anybody. So enjoy yourself as much as you can with the Parasailing programs at the Falcon Ridge Sky Leisure Society.</p>
    <svg class="service-arrow" width="40" height="14" viewBox="0 0 40 14"><path d="M0 7h37M31 1l6 6-6 6" fill="none" stroke="#b12f80" stroke-width="2.5"/></svg>
  </article>
</section>

<section class="fleet">
  <div class="fleet-frame"></div>
  <div class="fleet-photo" role="img" aria-label="Gyrocopters flying over a waterfront hotel and marina"></div>
  <h2>FLEET</h2>
  <div class="rule"></div>
  <p>Lorem ipsum dolor sit amet, consectetur adipiscing elit, sed do eiusmod tempor incididunt ut labore et dolore magna aliqua. Ut enim ad minim veniam, quis nostrud exercitation ullamco laboris nisi ut aliquip ex ea commodo consequat. Duis aute irure dolor in reprehenderit in voluptate velit esse cillum dolore eu fugiat nulla pariatur. Excepteur sint occaecat cupidatat non proident, sunt in culpa qui</p>
  <div class="outline-btn">Read More</div>
</section>

<section class="team">
  <h2 class="section-title">Meet the Team</h2>
  <div class="title-rule"></div>
  <article class="member" style="left:112px">
    <div class="member-photo" role="img" aria-label="Team member portrait" style="background:linear-gradient(180deg,#8c6a4a,#c9a13a 70%,#6b5640)"></div>
    <h4>Tessa Marlowe</h4><div class="role">Lorem ipsum</div>
    <div class="member-social"><i></i><i></i></div>
  </article>
  <article class="member" style="left:442px">
    <div class="member-photo" role="img" aria-label="Team member portrait" style="background:linear-gradient(180deg,#d8d8d8,#9a9a9a 60%,#2c3440)"></div>
    <h4>Tessa Marlowe</h4><div class="role">Lorem ipsum</div>
    <div class="member-social"><i></i><i></i></div>
  </article>
  <article class="member" style="left:770px">
    <div class="member-photo" role="img" aria-label="Team member portrait" style="background:linear-gradient(180deg,#b8bcc0,#c8a88a 55%,#56604a)"></div>
    <h4>Tessa Marlowe</h4><div class="role">Lorem ipsum</div>
    <div class="member-social"><i></i><i></i></div>
  </article>
  <div class="team-dots"><i class="on"></i><i></i><i></i><i></i></div>
</section>

<section class="bookings">
  <h2 class="section-title">Bookings</h2>
  <div class="title-rule"></div>
  <div class="bookings-copy">
    <p>Lorem ipsum dolor sit amet, consectetur adipiscing elit, sed do eiusmod tempor incididunt ut labore et dolore magna aliqua. Ut enim ad minim veniam, quis nostrud exercitation ullamco laboris nisi ut aliquip ex ea commodo consequat. Duis aute irure dolor in reprehenderit in voluptate velit esse cillum dolore eu fugiat nulla pariatur. Excepteur sint occaecat cupidatat non proident, sunt in culpa qui officia deserunt mollit anim id est laborum</p>
    <p>Lorem ipsum dolor sit amet, consectetur adipiscing elit, sed do eiusmod tempor incididunt ut labore et dolore magna aliqua. Ut enim ad minim veniam, quis nostrud exercitation ullamco laboris nisi ut aliquip ex ea commodo consequat. Duis aute irure dolor in reprehenderit in voluptate velit esse cillum dolore eu fugiat nulla pariatur. Excepteur sint occaecat cupidatat non proident, sunt in culpa qui officia deserunt mollit anim id est laborum</p>
  </div>
  <div class="btn">Book Now</div>
</section>

<section class="contact">
  <div class="contact-frame"></div>
  <div class="contact-photo" role="img" aria-label="Two pilots in helmets giving a thumbs up in a gyrocopter cockpit"></div>
  <h2>CONTACT US</h2>
</section>
<div class="field" style="left:598px;top:4296px;width:234px;height:50px">Name</div>
<div class="field" style="left:840px;top:4296px;width:236px;height:50px">Email</div>
<div class="field" style="left:598px;top:4366px;width:234px;height:50px">Phone</div>
<div class="field" style="left:840px;top:4366px;width:236px;height:50px">Subject</div>
<div class="field" style="left:598px;top:4434px;width:478px;height:50px;justify-content:space-between">Services<svg width="10" height="6" viewBox="0 0 10 6"><path d="M1 1l4 4 4-4" fill="none" stroke="#555" stroke-width="1.5"/></svg></div>
<div class="field area" style="left:598px;top:4502px;width:478px;height:96px">Message</div>
<div class="apply">APPLY TODAY <svg width="16" height="16" viewBox="0 0 16 16"><circle cx="8" cy="8" r="8" fill="#fff"/><path d="M6 4.5 9.5 8 6 11.5" fill="none" stroke="#3a86ab" stroke-width="2"/></svg></div>

<footer class="site-footer">
  <div class="newsletter-title">Subscribe to our newsletter to get important news &amp; amazing offers:</div>
  <div class="newsletter"><div class="email">Email</div><div class="sub">SUBSCRIBE</div></div>
  <div class="social"><i></i><i></i><i></i><i></i><i></i></div>
  <div class="footer-rule"></div>
  <nav class="footer-nav"><span>Home</span><span>About us</span><span>Services &amp; Price</span><span>Our Team</span><span>Fleet</span><span>Events</span><span>FAQ</span><span>Contact</span></nav>
  <div class="copyright">Copyrights © 2022 All Rights Reserved by FRSLS</div>
</footer>

</body>
</html>
```